Experienced and Professional Marriage Celebrant

I need a web design for my services as a marriage celebrant in the Sydney area. I want people to have the impression I am a modern and professional marriage celebrant who can tailor a wedding ceremony and execute the ceremony with a high level of care and accommodate and adapt to any style of wedding and personalities of couples. I like a mint and pink and black theme and I am not sure whether to use the professional photos of me, might be too stiff! But would like to see ideas you can come up with. Happy to use other photos you might have

Reason: I have haven't been able to respond as quickly as I would have liked this last week to comments so extending a few days. Thanks

```html
<!DOCTYPE html>
<html lang="en">
<head>
<meta charset="utf-8">
<title>Mira Lawson Celebrant</title>
<link rel="stylesheet" href="https://fonts.googleapis.com/css2?family=Roboto+Condensed:wght@400;700&family=Roboto:wght@400;700&display=swap">
<style>
  :root {
    --mint: #7fd06a;
    --pink: #ec3f8f;
    --ink: #1d1d1d;
    --charcoal: #333335;
    --dark: #262628;
    --nav: #3a3a3c;
    --text: #5a5a5a;
    --light-text: #c9c9c9;
    --white: #ffffff;
  }
  * { box-sizing: border-box; margin: 0; padding: 0; }
  html, body { width: 750px; height: 1200px; overflow: hidden; }
  body { background: var(--white); font-family: "Roboto", Arial, sans-serif; color: var(--text); position: relative; }

  .site-header { height: 45px; display: flex; align-items: center; justify-content: space-between; padding: 0 18px 0 20px; }
  .brand { font-family: "Roboto Condensed", Arial, sans-serif; font-weight: 700; font-size: 24px; color: var(--ink); letter-spacing: 0.5px; }
  .header-contact { display: flex; align-items: center; gap: 6px; font-family: "Roboto Condensed", Arial, sans-serif; font-size: 13px; color: var(--mint); font-weight: 700; }
  .header-contact .phone-number { color: var(--ink); }
  .social { display: flex; gap: 4px; margin-left: 6px; }
  .social span { width: 14px; height: 14px; border-radius: 50%; background: var(--pink); display: block; }

  .main-nav { height: 30px; background: var(--nav); display: flex; padding-left: 18px; }
  .main-nav a { font-family: "Roboto Condensed", Arial, sans-serif; font-size: 11.5px; color: var(--white); text-decoration: none; display: flex; align-items: center; padding: 0 16px; border-right: 1px solid #4c4c4e; }
  .main-nav a.active { background: var(--mint); }

  .hero { height: 270px; position: relative; background: linear-gradient(180deg, #c9d6df 0%, #8b99a6 35%, #3c4048 60%, #6fb6c4 78%, #2b2e33 100%); }
  .hero-dots { position: absolute; bottom: 18px; left: 50%; transform: translateX(-50%); display: flex; gap: 6px; }
  .hero-dots span { width: 8px; height: 8px; border-radius: 50%; background: rgba(255,255,255,0.55); }
  .hero-dots span.on { background: var(--white); }

  .section-title { font-family: "Roboto Condensed", Arial, sans-serif; font-weight: 700; font-size: 16px; color: var(--ink); text-transform: uppercase; }
  .section-title em { font-style: normal; color: var(--pink); font-weight: 400; }
  .on-dark .section-title { color: var(--white); }

  .button { display: inline-flex; align-items: stretch; height: 22px; font-family: "Roboto Condensed", Arial, sans-serif; font-size: 10px; font-weight: 700; color: var(--ink); text-decoration: none; }
  .button .label { background: var(--mint); padding: 0 12px; display: flex; align-items: center; }
  .button .arrow { background: var(--pink); width: 22px; display: flex; align-items: center; justify-content: center; }

  .welcome { height: 200px; padding: 30px 45px 0 45px; display: flex; gap: 22px; }
  .welcome-copy { width: 420px; }
  .welcome-copy p { font-size: 9.5px; line-height: 14px; margin: 10px 0 16px; }
  .welcome-photo { width: 222px; height: 145px; margin-top: 5px; background: linear-gradient(160deg, #e8e6df 0%, #9fc490 45%, #5d8f4f 100%); box-shadow: 6px 6px 0 var(--pink); }

  .services-band { height: 205px; background: var(--charcoal); padding: 22px 45px 0 45px; display: flex; gap: 22px; }
  .services { width: 465px; }
  .services-body { display: flex; gap: 10px; margin-top: 14px; }
  .services-photo { width: 155px; height: 135px; flex: none; background: linear-gradient(160deg, #c9a36a 0%, #8b4a4a 50%, #e6d2b4 100%); }
  .services-copy p { font-size: 9.5px; line-height: 14px; color: var(--light-text); margin-bottom: 14px; }
  .news { flex: 1; }
  .news-list { list-style: none; margin-top: 12px; }
  .news-item { display: flex; gap: 8px; margin-bottom: 9px; }
  .news-thumb { width: 40px; height: 32px; flex: none; background: linear-gradient(160deg, #a7b48c, #4f5a3c); }
  .news-item p { font-size: 8.5px; line-height: 11px; color: var(--light-text); }
  .news-item .date { color: var(--pink); display: block; margin-top: 2px; }
  .news-more { font-family: "Roboto Condensed", Arial, sans-serif; font-size: 10px; font-weight: 700; color: var(--mint); text-decoration: none; display: block; text-align: right; }

  .gallery { padding: 22px 45px 0; height: 278px; }
  .gallery .section-title { text-align: center; }
  .gallery-grid { display: grid; grid-template-columns: repeat(4, 1fr); grid-auto-rows: 72px; gap: 4px; margin-top: 12px; }
  .gallery-grid div:nth-child(1) { background: linear-gradient(160deg, #8fb6d8, #b88a62); }
  .gallery-grid div:nth-child(2) { background: linear-gradient(160deg, #4e5a66, #d9d2c6); }
  .gallery-grid div:nth-child(3) { background: linear-gradient(160deg, #cfc6a8, #6f7c5a); }
  .gallery-grid div:nth-child(4) { background: linear-gradient(160deg, #7c5a48, #2e2624); }
  .gallery-grid div:nth-child(5) { background: linear-gradient(160deg, #6fa3c8, #c07aa4); }
  .gallery-grid div:nth-child(6) { background: linear-gradient(160deg, #8fa0ae, #4d5a40); }
  .gallery-grid div:nth-child(7) { background: linear-gradient(160deg, #a9b8c6, #5c6b4e); }
  .gallery-grid div:nth-child(8) { background: linear-gradient(160deg, #caa58a, #5e3e33); }
  .gallery-grid div:nth-child(9) { background: linear-gradient(160deg, #d24f9b, #3b2a6b); }
  .gallery-grid div:nth-child(10) { background: linear-gradient(160deg, #b9b6ad, #535451); }
  .gallery-grid div:nth-child(11) { background: linear-gradient(160deg, #7a5b7e, #d8c4b0); }
  .gallery-grid div:nth-child(12) { background: linear-gradient(160deg, #dedad2, #2f3033); }

  .testimonials { padding: 14px 45px 0; height: 125px; }
  .testimonial { display: flex; gap: 14px; margin-top: 10px; }
  .testimonial-photo { width: 95px; height: 58px; flex: none; background: linear-gradient(160deg, #d9c7a8, #7f6a52); }
  .testimonial blockquote { font-size: 9.5px; line-height: 14px; font-style: italic; }
  .testimonial blockquote::before { content: "\201C"; color: var(--pink); font-size: 20px; font-style: normal; line-height: 0; vertical-align: -6px; margin-right: 3px; }
  .testimonial .read-more { font-size: 9px; color: var(--pink); font-weight: 700; text-decoration: none; display: inline-block; margin-top: 4px; }

  .site-footer { position: absolute; left: 0; right: 0; bottom: 0; height: 63px; background: var(--dark); display: flex; align-items: center; justify-content: space-between; padding: 0 45px; }
  .copyright { font-size: 8.5px; line-height: 13px; color: #9a9a9a; }
  .footer-connect { display: flex; align-items: center; gap: 8px; font-family: "Roboto Condensed", Arial, sans-serif; font-size: 10px; font-weight: 700; color: var(--white); }
  .footer-connect .social span { width: 18px; height: 18px; }
</style>
</head>
<body>

<header class="site-header">
  <div class="brand">MIRA LAWSON <span style="color:var(--ink)">CELEBRANT</span></div>
  <div class="header-contact">
    <svg width="12" height="12" viewBox="0 0 24 24" aria-hidden="true"><path fill="#7fd06a" d="M6.6 10.8a15.1 15.1 0 0 0 6.6 6.6l2.2-2.2c.3-.3.7-.4 1-.2 1.1.4 2.3.6 3.6.6.6 0 1 .4 1 1V20c0 .6-.4 1-1 1A17 17 0 0 1 3 4c0-.6.4-1 1-1h3.5c.6 0 1 .4 1 1 0 1.3.2 2.5.6 3.6.1.3 0 .7-.2 1z"/></svg>
    <span>CALL US:</span><span class="phone-number">123-555-0147</span>
    <div class="social"><span></span><span></span><span></span></div>
  </div>
</header>

<nav class="main-nav">
  <a class="active" href="#">HOME</a>
  <a href="#">ABOUT US</a>
  <a href="#">SERVICES</a>
  <a href="#">NEWS &amp; EVENTS</a>
  <a href="#">GALLERY</a>
  <a href="#">TESTIMONIALS</a>
  <a href="#">BLOG</a>
  <a href="#">CONTACT US</a>
</nav>

<section class="hero" role="img" aria-label="Wedding party with bride and groom celebrating outdoors">
  <div class="hero-dots"><span></span><span></span><span class="on"></span><span></span><span></span></div>
</section>

<section class="welcome">
  <div class="welcome-copy">
    <h2 class="section-title">Welcome to <em>Mira Lawson Celebrant</em></h2>
    <p>Every couple has a story worth telling well. I work closely with you to shape a ceremony that reflects who you are, whether you are planning a relaxed beach gathering, a garden celebration or a formal city wedding. From the first meeting to the final vows, I handle every detail with care so you can simply enjoy the moment together with the people you love.</p>
    <a class="button" href="#"><span class="label">READ MORE</span><span class="arrow"><svg width="8" height="8" viewBox="0 0 8 8"><path d="M2 1l3 3-3 3" stroke="#fff" stroke-width="1.5" fill="none"/></svg></span></a>
  </div>
  <div class="welcome-photo" role="img" aria-label="Outdoor garden ceremony set up on a lawn"></div>
</section>

<section class="services-band on-dark">
  <div class="services">
    <h2 class="section-title">Our <em>Services</em></h2>
    <div class="services-body">
      <div class="services-photo" role="img" aria-label="Decorated wedding reception room"></div>
      <div class="services-copy">
        <p>Ceremonies of every style, written around you. Choose a simple legal ceremony, a personal wedding with readings and rituals, a vow renewal or a naming day. Each service includes planning meetings, a rehearsal, all legal paperwork and a tailored script that suits your personalities and your venue.</p>
        <a class="button" href="#"><span class="label">READ MORE</span><span class="arrow"><svg width="8" height="8" viewBox="0 0 8 8"><path d="M2 1l3 3-3 3" stroke="#fff" stroke-width="1.5" fill="none"/></svg></span></a>
      </div>
    </div>
  </div>
  <div class="news">
    <h2 class="section-title">News <em>&amp; Events</em></h2>
    <ul class="news-list">
      <li class="news-item"><div class="news-thumb" role="img" aria-label="Wedding venue"></div><p>Wedding open day at Harbour Gardens this spring<span class="date">Aug 20, 2015</span></p></li>
      <li class="news-item"><div class="news-thumb" role="img" aria-label="Couple at ceremony"></div><p>New vow renewal packages now available<span class="date">Aug 12, 2015</span></p></li>
      <li class="news-item"><div class="news-thumb" role="img" aria-label="Wedding rings"></div><p>Tips for writing your own wedding vows<span class="date">Aug 03, 2015</span></p></li>
    </ul>
    <a class="news-more" href="#">LEARN MORE &rsaquo;</a>
  </div>
</section>

<section class="gallery">
  <h2 class="section-title">Photo <em>Gallery</em></h2>
  <div class="gallery-grid">
    <div role="img" aria-label="Beach wedding ceremony"></div>
    <div role="img" aria-label="Couple under an arch"></div>
    <div role="img" aria-label="Outdoor wedding guests"></div>
    <div role="img" aria-label="Couple holding hands"></div>
    <div role="img" aria-label="Reception with pink lighting"></div>
    <div role="img" aria-label="Ceremony on a lawn"></div>
    <div role="img" aria-label="Garden reception tables"></div>
    <div role="img" aria-label="Couple exchanging rings"></div>
    <div role="img" aria-label="Evening reception hall"></div>
    <div role="img" aria-label="Formal reception tables"></div>
    <div role="img" aria-label="Wedding dance"></div>
    <div role="img" aria-label="Wedding party group"></div>
  </div>
</section>

<section class="testimonials">
  <h2 class="section-title">Our <em>Testimonials</em></h2>
  <div class="testimonial">
    <div class="testimonial-photo" role="img" aria-label="Happy couple on their wedding day"></div>
    <div>
      <blockquote>Mira made our day feel so personal and calm. She listened to our story, wrote a ceremony that had our families laughing and crying, and guided us through every step with warmth. We could not have asked for a better celebrant for our wedding.</blockquote>
      <a class="read-more" href="#">READ MORE</a>
    </div>
  </div>
</section>

<footer class="site-footer">
  <p class="copyright">Copyright &copy; 2015 | Mira Lawson Celebrant<br>All Rights Reserved</p>
  <div class="footer-connect">CONNECT US
    <div class="social"><span></span><span></span><span></span></div>
  </div>
</footer>

</body>
</html>
```